QorLa Drift Bhutan Trip

This is a one-page (A5) flyer to attract sign ups for Bhutan Trip.

Target Market(s)

Young entrepreneurs (worldwide)

Requirements
Must have
• Must have "WOW" effect and attract sign ups
Nice to have
• Striking and vibrant

```html
<!DOCTYPE html>
<html lang="en">
<head>
<meta charset="utf-8">
<title>QorLa Drift Bhutan Trip</title>
<link rel="stylesheet" href="https://fonts.googleapis.com/css2?family=Bangers&family=Roboto+Condensed:ital,wght@0,400;0,700;1,700;1,900&family=Roboto:wght@300;400;900&display=swap">
<style>
  :root{
    --sky-light:#ffffff;
    --sky:#8fd4ef;
    --orange:#f38f3a;
    --red:#e41e2b;
    --lime:#bfd631;
    --tick:#8cd23c;
    --ink:#1c1c1c;
    --cream:#fff5c2;
    --navy:#2a3c8f;
    --white:#ffffff;
    --page:#e9e9e9;
    --t-orange:#f47a20;
    --t-red:#e3262b;
    --t-green:#8cc63f;
    --t-blue:#22a8d8;
    --t-pink:#ef6aa8;
    --t-magenta:#c81f8a;
  }
  *{box-sizing:border-box;margin:0;padding:0}
  html,body{width:1200px;height:1200px;overflow:hidden;background:var(--page)}
  .flyer{position:absolute;left:177px;top:0;width:846px;height:1200px;overflow:hidden;background:var(--white);font-family:"Roboto Condensed",sans-serif}

  .sky{position:absolute;left:0;top:0;width:846px;height:640px;
    background:radial-gradient(ellipse 70% 60% at 50% 8%,var(--sky-light) 0%,#d9f1fb 35%,var(--sky) 100%)}
  .presenter{position:absolute;top:52px;width:100%;text-align:center;font-family:"Roboto",sans-serif;font-weight:300;font-size:20px;color:#333;letter-spacing:.3px}
  .host-name{position:absolute;top:110px;width:100%;text-align:center;font-family:"Roboto Condensed",sans-serif;font-weight:700;font-size:56px;color:var(--ink);line-height:1}
  .title{position:absolute;top:222px;width:100%;text-align:center;font-family:"Bangers",sans-serif;font-size:128px;letter-spacing:4px;line-height:1;
    text-shadow:3px 3px 0 var(--white),-2px -2px 0 var(--white),2px -2px 0 var(--white),-2px 2px 0 var(--white),5px 6px 8px rgba(0,0,0,.35)}
  .title .o{color:var(--t-orange)} .title .r{color:var(--t-red)} .title .g{color:var(--t-green)}
  .title .b{color:var(--t-blue)} .title .p{color:var(--t-pink)} .title .m{color:var(--t-magenta)}
  .title .k{color:var(--ink)}
  .date{position:absolute;top:368px;width:100%;text-align:center;font-family:"Bangers",sans-serif;font-size:48px;color:var(--t-red);letter-spacing:3px;transform:skewX(-8deg)}

  .photo{position:absolute;background:var(--white);padding:10px;box-shadow:3px 4px 10px rgba(0,0,0,.35)}
  .photo .fill{width:100%;height:100%}
  .photo-1{left:8px;top:468px;width:218px;height:210px;transform:rotate(-5deg)}
  .photo-1 .fill{background:linear-gradient(180deg,#9fb7cc 0%,#b8433a 45%,#e8e2d6 65%,#b9ab98 100%)}
  .photo-2{left:228px;top:462px;width:202px;height:210px;transform:rotate(2deg)}
  .photo-2 .fill{background:linear-gradient(180deg,#6e6a62 0%,#5a4a44 50%,#7a6a60 100%)}
  .photo-3{left:416px;top:478px;width:218px;height:212px;transform:rotate(-4deg)}
  .photo-3 .fill{background:linear-gradient(180deg,#c9d9e6 0%,#5d8a46 38%,#9b3a2e 62%,#e8e4dc 100%)}
  .photo-4{left:632px;top:462px;width:214px;height:218px;transform:rotate(6deg)}
  .photo-4 .fill{background:linear-gradient(180deg,#d7e5ec 0%,#5f8f43 40%,#4f7a37 70%,#9aa39a 100%)}

  .band-curve{position:absolute;left:0;top:604px}
  .signup{position:absolute;left:0;top:620px;width:846px;height:162px;background:var(--orange)}
  .signup-head{position:absolute;left:32px;top:20px;font-family:"Roboto Condensed",sans-serif;font-weight:900;font-style:italic;font-size:104px;color:var(--cream);line-height:1;
    -webkit-text-stroke:2px var(--t-red);text-shadow:3px 3px 4px rgba(0,0,0,.3)}
  .signup-swoosh{position:absolute;left:126px;top:128px}
  .signup-brace{position:absolute;left:436px;top:18px}
  .signup-text{position:absolute;left:482px;top:26px;width:340px;font-size:31px;line-height:37px;color:var(--white)}

  .highlights{position:absolute;left:0;top:782px;width:846px;height:262px;background:var(--red)}
  .hl-label{position:absolute;left:38px;top:236px;transform:rotate(-90deg);transform-origin:0 0;font-family:"Roboto",sans-serif;font-weight:900;font-size:22px;letter-spacing:5px;color:var(--white)}
  .hl-list{position:absolute;left:68px;top:12px;list-style:none}
  .hl-list li{display:flex;align-items:center;height:40px;font-size:24px;color:var(--white);white-space:nowrap}
  .hl-list svg{width:32px;height:32px;margin-right:14px;flex:none}
  .hl-list b{font-weight:700;margin-right:6px}

  .price{position:absolute;left:551px;top:778px;width:270px;height:258px}
  .price-text{position:absolute;left:551px;top:806px;width:270px;text-align:center;font-family:"Roboto",sans-serif;color:var(--ink)}
  .price-label{font-size:21px;line-height:24px}
  .price-main{font-weight:900;font-size:38px;line-height:40px}
  .price-rule{width:190px;height:2px;background:#d9e87a;margin:6px auto 6px}
  .price-early{font-size:18px;line-height:22px}
  .price-big{font-weight:900;font-size:46px;line-height:48px}
  .price-note{font-size:12px;line-height:16px}

  .footer{position:absolute;left:0;top:1044px;width:846px;height:156px;background:var(--white)}
  .supported{position:absolute;left:54px;top:20px;font-family:"Roboto",sans-serif;font-size:15px;color:var(--ink)}
  .partner{position:absolute;top:62px;display:flex;align-items:center;gap:8px;font-family:"Roboto",sans-serif;font-weight:400;font-size:18px}
  .partner-1{left:60px;color:#3c9a3e}
  .partner-2{left:226px;color:#2f7d8a}
  .partner-3{left:400px;color:#1f4d8a}
  .partner .dot{width:34px;height:34px;border-radius:50%;border:3px solid currentColor}
  .footer-divider{position:absolute;left:506px;top:22px;width:2px;height:110px;background:var(--navy)}
  .register{position:absolute;left:520px;top:28px;width:320px;text-align:center;font-family:"Roboto",sans-serif}
  .register-head{font-weight:900;font-style:italic;font-size:34px;color:var(--ink);line-height:40px}
  .register-limit{font-size:22px;color:var(--red);line-height:30px}
  .register-mail{font-size:22px;color:var(--navy);line-height:30px}
</style>
</head>
<body>
<main class="flyer">
  <section class="sky">
    <p class="presenter">Exclusively Brought To You By:</p>
    <p class="host-name">QorLa Drift</p>
    <h1 class="title"><span class="o">B</span><span class="r">H</span><span class="g">U</span><span class="b">T</span><span class="p">A</span><span class="m">N</span> <span class="k">TRIP</span></h1>
    <p class="date">3-6 JULY 2017</p>
  </section>

  <figure class="photo photo-1"><div class="fill" role="img" aria-label="Bhutanese temple with red roofs and a monk crossing the courtyard"></div></figure>
  <figure class="photo photo-2"><div class="fill" role="img" aria-label="Group photo of trip participants in traditional dress"></div></figure>
  <figure class="photo photo-3"><div class="fill" role="img" aria-label="Punakha dzong fortress beneath green hills"></div></figure>
  <figure class="photo photo-4"><div class="fill" role="img" aria-label="Suspension bridge with prayer flags in a mountain valley"></div></figure>

  <svg class="band-curve" width="846" height="20" viewBox="0 0 846 20"><path d="M0 20 Q423 0 846 20 Z" fill="var(--orange)"/></svg>
  <section class="signup">
    <h2 class="signup-head">SIGN UP</h2>
    <svg class="signup-swoosh" width="296" height="20" viewBox="0 0 296 20"><path d="M0 18 Q148 4 296 8 L294 16 Q148 10 0 18 Z" fill="var(--white)"/></svg>
    <svg class="signup-brace" width="26" height="126" viewBox="0 0 26 126"><path d="M2 2 Q14 2 14 20 L14 50 Q14 62 24 63 Q14 64 14 76 L14 106 Q14 124 2 124" fill="none" stroke="var(--white)" stroke-width="2"/></svg>
    <p class="signup-text">for a once in a lifetime experience in the land of happiness!</p>
  </section>

  <section class="highlights">
    <span class="hl-label">HIGHLIGHTS</span>
    <ul class="hl-list">
      <li><svg viewBox="0 0 32 32"><path d="M3 17 L12 26 L29 5" fill="none" stroke="var(--tick)" stroke-width="5"/></svg><b>LEARN</b>from Leading Social Change Makers</li>
      <li><svg viewBox="0 0 32 32"><path d="M3 17 L12 26 L29 5" fill="none" stroke="var(--tick)" stroke-width="5"/></svg><b>ENGAGE</b>the community through volunteering</li>
      <li><svg viewBox="0 0 32 32"><path d="M3 17 L12 26 L29 5" fill="none" stroke="var(--tick)" stroke-width="5"/></svg><b>DISCOVER</b>your inner happiness</li>
      <li><svg viewBox="0 0 32 32"><path d="M3 17 L12 26 L29 5" fill="none" stroke="var(--tick)" stroke-width="5"/></svg><b>SAVOUR</b>organic food</li>
      <li><svg viewBox="0 0 32 32"><path d="M3 17 L12 26 L29 5" fill="none" stroke="var(--tick)" stroke-width="5"/></svg><b>IMMERSE</b>in traditional sports and craft</li>
      <li><svg viewBox="0 0 32 32"><path d="M3 17 L12 26 L29 5" fill="none" stroke="var(--tick)" stroke-width="5"/></svg><b>EXPERIENCE</b>warm Bhutanese hospitality</li>
    </ul>
  </section>

  <svg class="price" viewBox="0 0 270 258">
    <path d="M135 2 C208 2 266 58 266 128 C266 160 262 190 256 212 C200 216 130 226 88 256 C38 230 4 186 4 128 C4 58 62 2 135 2 Z" fill="var(--lime)"/>
  </svg>
  <div class="price-text">
    <p class="price-label">PRICE AT</p>
    <p class="price-main">USD 2800</p>
    <div class="price-rule"></div>
    <p class="price-early">EARLY BIRD DISCOUNT</p>
    <p class="price-big">USD 2300</p>
    <p class="price-note">(If you sign up by 31 March 2017)</p>
  </div>

  <footer class="footer">
    <p class="supported">SUPPORTED BY</p>
    <div class="partner partner-1"><span class="dot"></span>Lumen Circle</div>
    <div class="partner partner-2">Trailwise</div>
    <div class="partner partner-3">Rootfield</div>
    <div class="footer-divider"></div>
    <div class="register">
      <p class="register-head">REGISTER NOW!</p>
      <p class="register-limit">Limited to 30 participants!</p>
      <p class="register-mail">Email: hana@lumencircle.org</p>
    </div>
  </footer>
</main>
</body>
</html>
```